Thornbury Fields Enterprise
Home grown grain fed beef Wholes, Halfs, Quarters
Locally raised
No Added Hormones
Call or text now to order (555) -0193-7720

```html
<!DOCTYPE html>
<html lang="en">
<head>
<meta charset="utf-8">
<title>Thornbury Fields Enterprise – Grain Fed Beef</title>
<link rel="stylesheet" href="https://fonts.googleapis.com/css2?family=DM+Serif+Display&family=Oswald:wght@500;600&family=Poppins:ital,wght@0,700;1,700&family=Roboto:wght@300&display=swap">
<style>
  :root {
    --page: #ffffff;
    --ink-dark: #1b1512;
    --photo-dark: #17110f;
    --photo-mid: #2a1e19;
    --meat: #a8353a;
    --wood: #6b3f22;
    --yellow: #fff200;
    --frame-red: #b3141d;
    --white: #ffffff;
    --pill-peach: #f6d9c5;
    --cross-red: #e3262b;
  }
  * { margin: 0; padding: 0; box-sizing: border-box; }
  html, body {
    width: 1200px; height: 862px; overflow: hidden;
    background: var(--page);
  }
  .flyer {
    position: absolute; left: 0; top: 7px;
    width: 1200px; height: 847px;
    overflow: hidden;
    background: var(--photo-dark);
  }
  .flyer-photo {
    position: absolute; inset: 0;
    background:
      radial-gradient(ellipse 32% 42% at 73% 70%, var(--meat) 0%, rgba(168,53,58,0.55) 45%, rgba(168,53,58,0) 100%),
      linear-gradient(180deg, rgba(0,0,0,0) 80%, var(--wood) 100%),
      linear-gradient(90deg, var(--photo-dark) 0%, var(--photo-mid) 70%, var(--photo-dark) 100%);
  }
  .brand {
    position: absolute; left: 20px; top: 56px; width: 600px;
    text-align: center;
    font-family: "DM Serif Display", serif;
    font-size: 76px; line-height: 76px;
    color: var(--white);
    letter-spacing: -0.5px;
  }
  .offer-box {
    position: absolute; left: 56px; top: 269px;
    width: 491px; height: 446px;
    border: 1.5px solid var(--frame-red);
    text-align: center;
  }
  .offer-kicker {
    margin-top: 34px;
    font-family: "Oswald", sans-serif; font-weight: 600;
    font-size: 58px; line-height: 62px;
    color: var(--yellow);
  }
  .offer-title {
    font-family: "Oswald", sans-serif; font-weight: 600;
    font-size: 76px; line-height: 78px;
    color: var(--yellow);
  }
  .offer-sizes {
    margin-top: 2px;
    font-family: "Poppins", sans-serif; font-weight: 700;
    font-size: 32px; line-height: 40px;
    color: var(--yellow);
  }
  .order-call {
    margin-top: 40px;
    font-family: "Roboto", sans-serif; font-weight: 300;
    font-size: 38px; line-height: 41px;
    color: var(--white);
  }
  .order-phone {
    position: absolute; left: 53px; top: 344px;
    width: 349px; height: 61px;
    border-radius: 31px;
    background: var(--pill-peach);
    font-family: "Oswald", sans-serif; font-weight: 600;
    font-size: 42px; line-height: 61px;
    color: var(--ink-dark);
  }
  .badge-local {
    position: absolute; left: 78px; top: 767px;
    display: flex; align-items: center; gap: 9px;
    font-family: "Poppins", sans-serif; font-weight: 700; font-style: italic;
    font-size: 21px; color: var(--white);
  }
  .badge-hormones {
    position: absolute; left: 317px; top: 769px;
    width: 348px; height: 51px;
    border-radius: 10px 26px 26px 10px;
    background: var(--yellow);
    display: flex; align-items: center; gap: 8px; padding-left: 20px;
    font-family: "Poppins", sans-serif; font-weight: 700;
    font-size: 22px; color: var(--ink-dark);
  }
</style>
</head>
<body>
  <main class="flyer">
    <div class="flyer-photo" role="img" aria-label="Photograph of a butcher's hands slicing a large bone-in tomahawk rib steak on a wooden board with rosemary and peppercorns, dark background"></div>

    <h1 class="brand">Thornbury Fields<br>Enterprise</h1>

    <section class="offer-box">
      <p class="offer-kicker">HOME GROWN</p>
      <p class="offer-title">GRAIN FED BEEF</p>
      <p class="offer-sizes">Wholes, Halfs, Quarters</p>
      <p class="order-call">Call or Text<br>Now to Order</p>
      <p class="order-phone">(555) -0193-7720</p>
    </section>

    <div class="badge-local">
      <svg width="44" height="44" viewBox="0 0 44 44" aria-hidden="true">
        <circle cx="22" cy="22" r="19" fill="none" stroke="var(--yellow)" stroke-width="4"/>
        <path d="M12 22 L20 31 L36 7" fill="none" stroke="var(--white)" stroke-width="5" stroke-linecap="round" stroke-linejoin="round"/>
      </svg>
      <span>Locally raised.</span>
    </div>

    <div class="badge-hormones">
      <svg width="30" height="30" viewBox="0 0 30 30" aria-hidden="true">
        <path d="M5 5 L25 25 M25 5 L5 25" stroke="var(--cross-red)" stroke-width="6" stroke-linecap="round"/>
      </svg>
      <span>No Added Hormones</span>
    </div>
  </main>
</body>
</html>
```